Dry Cleaners Pick-up & Delivery Service

We are in the need of a post card design to hand out in public focused in our dry-cleaners pick up and delivery business services. The postcard must include a price list of most common items sent to the dry cleaners on a regular basis along with promotional sign-up deals and specials as advertised on our website. The color palette must match our website's color scheme - www.vostrelin.com - we would like to focus on our free pick-up and free delivery service. The hand out post card should look clean, organized and neat, yet modern in style projecting the cleanliness of the clothing articles that our customer let us take care of saving them time while we take care of this errand for them. All new customers receive a free high quality, heavy duty laundry bag with our business information and are encouraged to request for $10 of free dry cleaning on their first order, no strings attached, just for signing up to our service.We strive to please our customers and invest on them to have more free time on their hands, plain and simple. We also offer law enforcement uniform special, as the area we focus our routes is a high law enforcement residential community. The logo is attached and must be visible in the postcard as well as the website address and phone number 305-472-1936 as these are the main contact forms of clients reaching our business. This is home based business, we have a partnership with a dry cleaners business who does all of our route customers' dry cleaning needs. Our business is all about the marketing, sales and networking with corporate businesses. The postcard handout must have designs of both sides of the post card as well. They will not be used for mailing for the moment being, they will be only used to hand out.

Industry/Entity Type

Dry Cleaning

```html
<!DOCTYPE html>
<html lang="en">
<head>
<meta charset="utf-8">
<title>Vostrelin Postcard</title>
<link href="https://fonts.googleapis.com/css2?family=Audiowide&family=Source+Sans+3:wght@400;600&display=swap" rel="stylesheet">
<style>
:root{
  --stage:#1c1c1c;
  --ink:#1e1e1e;
  --panel-dark:#2b2b2b;
  --green:#78c24a;
  --green-deep:#4fae2b;
  --paper:#ffffff;
  --muted:#666;
  --rule:#cfcfcf;
}
*{margin:0;padding:0;box-sizing:border-box}
html,body{width:1200px;height:1170px;overflow:hidden;background:var(--stage)}
body{font-family:"Source Sans 3",Arial,sans-serif;color:var(--ink)}
.stage{position:relative;width:1200px;height:1170px}
.card{position:absolute;background:var(--paper);overflow:hidden}
.abs{position:absolute}

/* brand lockup */
.brand{position:absolute;text-align:center}
.brand-name{display:inline-flex;align-items:center;gap:14px;font-family:"Source Sans 3",sans-serif;font-weight:600;color:var(--ink);font-size:54px;line-height:1}
.brand-mark{width:18px;height:18px;background:var(--green-deep)}
.brand-tagline{font-size:22px;color:var(--ink);margin-top:14px;letter-spacing:.3px}

.cta-dark{position:absolute;background:var(--panel-dark);border-radius:4px;text-align:center;font-family:"Audiowide",sans-serif}
.cta-dark .cta-top{color:#fff}
.cta-dark .cta-url{color:var(--green)}
.cta-green{position:absolute;background:var(--green);border-radius:4px;text-align:center;font-family:"Audiowide",sans-serif;color:#fff}
.cta-green .cta-sub{color:var(--ink)}

/* back side */
.card-back{left:57px;top:60px;width:695px;height:540px}
.back-photo{position:absolute;inset:0;background:linear-gradient(180deg,#fff 0%,#f7f8fa 30%,#dfe6ef 60%,#bfcde0 100%)}
.card-back .brand{left:0;right:0;top:42px}
.back-footer{position:absolute;left:0;right:0;bottom:0;height:58px;background:#0d0d0d;color:var(--green);font-size:16px;padding:16px 0 0 35px}

/* front side */
.card-front{left:127px;top:388px;width:1007px;height:782px}
.card-front .brand{left:60px;width:390px;top:70px}
.feature-art{position:absolute;left:55px;top:236px;width:115px;height:102px;background:linear-gradient(135deg,#e9edf2,#5fae3c);border-radius:6px}
.badge-shape{position:absolute;left:52px;top:376px;width:118px;height:118px;border-radius:50%;background:#1f1f1f;border:4px solid var(--green)}
.dollar{position:absolute;left:70px;top:505px;font-size:130px;line-height:1;font-weight:600;color:var(--green)}
.feature{position:absolute;left:192px;width:395px}
.feature h2{font-family:"Audiowide",sans-serif;font-weight:400;color:var(--green);font-size:23px;line-height:39px;letter-spacing:.5px}
.feature p{font-size:16.5px;line-height:21px;color:#222}

.offer{position:absolute;left:600px;width:370px;top:196px;text-align:center;font-size:20px;line-height:24px}
.pricing-kicker{position:absolute;left:607px;top:251px;font-size:7.5px;color:var(--green-deep);letter-spacing:.3px}
.pricing-rule-top{position:absolute;left:598px;top:262px;width:350px;height:1px;background:var(--rule)}
.pricing-rule-side{position:absolute;left:591px;top:268px;width:1px;height:410px;background:var(--rule)}
.pricing-title{position:absolute;left:607px;top:273px;font-family:"Audiowide",sans-serif;font-size:14px;color:#777;letter-spacing:1px}
.pricing-rule-title{position:absolute;left:598px;top:292px;width:350px;height:1px;background:var(--rule)}

.price-item{position:absolute;width:190px}
.item-name{font-size:10px;line-height:11px;color:#222}
.item-note{font-size:6px;line-height:7px;color:#444}
.price{position:absolute;top:1px;width:44px;height:14px;border-radius:7px;background:var(--green);color:#fff;font-size:9.5px;line-height:14px;padding-left:5px}
.col-left .price{left:103px}
.col-right .price{left:107px}
.combo-text{position:absolute;left:784px;font-size:9.5px;line-height:15px;color:#222}

.fineprint{position:absolute;left:607px;width:340px;font-size:5.5px;line-height:10px;color:#777}
.more-info{position:absolute;left:607px;top:660px;font-family:"Audiowide",sans-serif;font-size:14px;letter-spacing:1.5px;color:var(--green)}

.front-footer{position:absolute;left:0;right:0;bottom:0;height:88px;background:#0d0d0d;color:var(--green);font-size:24px;text-align:center;padding-top:14px}
.footer-notch{position:absolute;left:774px;bottom:86px;width:0;height:0;border-left:10px solid transparent;border-right:10px solid transparent;border-top:10px solid var(--paper);transform:translateY(10px)}
</style>
</head>
<body>
<div class="stage">

  <section class="card card-back" aria-label="Postcard back side">
    <div class="back-photo" role="img" aria-label="Photo of pressed shirts on hangers in soft blue and white tones"></div>
    <div class="brand">
      <div class="brand-name"><span class="brand-mark"></span>Vostrelin</div>
      <div class="brand-tagline">Dry Cleaners Pick-up &amp; Delivery Services, LLC</div>
    </div>
    <div class="cta-dark" style="left:177px;top:218px;width:366px;height:74px;padding-top:10px">
      <div class="cta-top" style="font-size:22px">Sign-up free!</div>
      <div class="cta-url" style="font-size:20px;margin-top:4px">www.Vostrelin.com</div>
    </div>
    <div class="cta-green" style="left:177px;top:296px;width:366px;height:70px;padding-top:14px">
      <div style="font-size:22px">Call 305-472-1936</div>
    </div>
    <div class="back-footer">2280 SW 94th Ct Miami FL 33165 us</div>
  </section>

  <section class="card card-front" aria-label="Postcard front side">
    <div class="brand">
      <div class="brand-name"><span class="brand-mark"></span>Vostrelin</div>
      <div class="brand-tagline">Dry Cleaners Pick-up &amp; Delivery Services, LLC</div>
    </div>

    <div class="feature-art" role="img" aria-label="Illustration of a delivery man holding folded laundry and a green laundry bag"></div>
    <div class="badge-shape" role="img" aria-label="Satisfaction guarantee seal"></div>
    <div class="dollar" aria-hidden="true">$</div>

    <div class="feature" style="top:210px">
      <h2>Free Pick-up &amp;<br>Delivery Dry-cleaning</h2>
      <p>Our delivery service is FREE of charge, even if it is a next-day service request, all you pay is for your dry cleaning or laundry service.<br>No hidden delivery fees.</p>
    </div>
    <div class="feature" style="top:375px">
      <h2>Fast dependable Service</h2>
      <p>You can rest assured that we will take good care of your items like they were ours! Customer service is at the top of our list and satisfaction is guaranteed!</p>
    </div>
    <div class="feature" style="top:508px">
      <h2>Save time and Money</h2>
      <p>We know what it's like to have to deal with your daily errands in your daily life and how extended work hours come into play. Save the hassle of having to drop and pick-up your clothes and let us pamper you a little bit. Enjoy more your well deserved time-off with your family from now on!</p>
    </div>

    <div class="cta-dark" style="left:599px;top:47px;width:345px;height:70px;padding-top:8px">
      <div class="cta-top" style="font-size:21px">Sign-up free!</div>
      <div class="cta-url" style="font-size:19px;margin-top:5px">www.Vostrelin.com</div>
    </div>
    <div class="cta-green" style="left:599px;top:119px;width:345px;height:69px;padding-top:14px">
      <div style="font-size:22px">Call 305-472-1936</div>
      <div class="cta-sub" style="font-size:13px;margin-top:2px">next-day service available!</div>
    </div>
    <div class="offer">Ask about getting $10 off your<br>first dry-cleaning order!</div>

    <div class="pricing-kicker">MOST COMMON CLOTHING ITEMS</div>
    <div class="pricing-rule-top"></div>
    <div class="pricing-rule-side"></div>
    <div class="pricing-title">DRY CLEANING PRICING</div>
    <div class="pricing-rule-title"></div>

    <div class="col-left">
      <div class="price-item" style="left:605px;top:303px"><div class="item-name">Women Dress</div><div class="item-note">Dry-Cleaned and Pressed -<br>Subject to surcharge (beads, etc)</div><span class="price">$10.95</span></div>
      <div class="price-item" style="left:605px;top:335px"><div class="item-name">Women Blouse</div><div class="item-note">Dry-Cleaned and Pressed</div><span class="price">$4.95</span></div>
      <div class="price-item" style="left:605px;top:364px"><div class="item-name">Women Casual Pants/</div><div class="item-name">Jeans <span class="item-note">Dry-Cleaned &amp; Pressed</span></div><span class="price">$4.95</span></div>
      <div class="price-item" style="left:605px;top:393px"><div class="item-name">Skirt - Long</div><div class="item-note">Dry-Cleaned and Pressed</div><span class="price">$6.49</span></div>
      <div class="price-item" style="left:605px;top:420px"><div class="item-name">Skirt - Short</div><div class="item-note">Dry-Cleaned and Pressed</div><span class="price">$4.95</span></div>
      <div class="price-item" style="left:605px;top:451px"><div class="item-name">Women Suit</div><div class="item-note">2 piece - Dry-Cleaned &amp; Pressed</div><span class="price">$10.95</span></div>
      <div class="price-item" style="left:605px;top:481px"><div class="item-name">Women Evening/</div><div class="item-name">Formal Dress - From:</div><div class="item-note">Subject to surcharge (beads, etc)</div><span class="price">$15.99</span></div>
      <div class="price-item" style="left:605px;top:524px"><div class="item-name">Men's Shirt <span class="item-note">(100% cotton)</span></div><div class="item-note">Laundered &amp; Pressed</div><span class="price">$2.99</span></div>
      <div class="price-item" style="left:605px;top:555px"><div class="item-name">Men Business Shirt</div><div class="item-note">Dry-Cleaned &amp; Pressed</div><span class="price">$4.5</span></div>
      <div class="price-item" style="left:605px;top:585px"><div class="item-name">Men Business Pants</div><div class="item-note">Dry-Cleaned &amp; Pressed</div><span class="price">$4.95</span></div>
    </div>

    <div class="col-right">
      <div class="price-item" style="left:784px;top:303px"><div class="item-name">Men Business Vest</div><div class="item-note">Dry-Cleaned &amp; Pressed</div><span class="price">$4.95</span></div>
      <div class="price-item" style="left:784px;top:333px"><div class="item-name">Men Pants/Jeans</div><div class="item-note">Dry-Cleaned &amp; Pressed</div><span class="price">$4.95</span></div>
      <div class="price-item" style="left:784px;top:364px"><div class="item-name">Men Suit</div><div class="item-note">2-Piece - Dry-Cleaned &amp; Pressed</div><span class="price">$10.95</span></div>
      <div class="price-item" style="left:784px;top:393px"><div class="item-name">3 piece suit</div><div class="item-note">Dry-Cleaned &amp; Pressed</div><span class="price">$15.95</span></div>
      <div class="price-item" style="left:784px;top:420px"><div class="item-name">Ties</div><div class="item-note">Dry-Cleaned &amp; Pressed</div><span class="price">$3.95</span></div>
      <div class="price-item" style="left:784px;top:449px"><div class="item-name">Sports Coat/Jacket</div><div class="item-note">Dry-Cleaned &amp; Pressed</div><span class="price">$6.95</span></div>
      <div class="price-item" style="left:784px;top:480px"><div class="item-name">Men Guayabera</div><div class="item-note">Laundered and Pressed</div><span class="price">$6.99</span></div>
      <div class="price-item" style="left:784px;top:511px"><div class="item-name">LAW ENFORCEMENT</div><span class="price">$7.99</span></div>
    </div>
    <div class="combo-text" style="top:524px">OFFICER / MILITARY COMBO SPECIAL!</div>
    <div class="combo-text" style="top:546px;left:783px">1 LEO or Military shirt with 1 LEO or<br>Military pair of pants</div>
    <div class="combo-text" style="top:580px">combination - Dry-Cleaned and<br>Pressed - Thank you for your service!</div>

    <div class="fineprint" style="top:617px">*Items that are silk, linen or lint are subject to a surcharge of up to $3.00 for each of those items in your order.</div>
    <div class="fineprint" style="top:630px">*Items that have beads or garments with attached accessories are subject to a surcharge of up to $4.00 for each garment in your order with such attachments. Varies depending on the volume attached to the garment.</div>
    <div class="more-info">For more info login our website</div>

    <div class="front-footer">2280 SW 94th Ct Miami FL 33165 us &nbsp;|&nbsp; 305-472-1936 &nbsp;|&nbsp; deliveryservice@vostrelin.com</div>
    <div class="footer-notch"></div>
  </section>

</div>
</body>
</html>
```